Private Optometric Practice Needs new Presentation Folders/Stationary

We recently moved our office and are looking to refresh our presentation folders and stationary. I tend to prefer simple, clean designs. We are a full scope optometric practice provide high quality eyewear, custom contact lenses, along with emergency care and treatment for dry eyes. We communicate with a lot of other doctors and want to exude professionalism. I have attached 2 versions of our logo.

Target Market(s)

Familys

Industry/Entity Type

Eyecare

Font styles to use
Sans Serif

Colors
0054AA
0677BA
7BADD7
CADEEF
E8F1F8

Requirements
Nice to have
• Bifold, areas to put information about practice, welcome letter

```html
<!DOCTYPE html>
<html lang="en">
<head>
<meta charset="utf-8">
<title>Northgate Vision – Stationery</title>
<link href="https://fonts.googleapis.com/css2?family=Montserrat:wght@300;400&display=swap" rel="stylesheet">
<style>
  :root {
    --backdrop: #c9c8cc;
    --paper: #ffffff;
    --footer-band: #e9e9e7;
    --ink-grey: #6d6e70;
    --ink-dark: #3a3b3d;
    --brand-blue: #2f9fe0;
    --motif-light: #a9d4f0;
    --motif-dark: #2f6f99;
    --folder-navy: #041a26;
    --folder-fold: #0b2735;
    --folder-text: #9fb3c2;
  }
  html, body {
    margin: 0;
    width: 1200px;
    height: 1000px;
    overflow: hidden;
    background: var(--backdrop);
    font-family: "Montserrat", Arial, sans-serif;
  }
  .canvas {
    position: relative;
    width: 1200px;
    height: 1000px;
  }

  /* Letterhead */
  .letterhead {
    position: absolute;
    left: 70px;
    top: 56px;
    width: 374px;
    height: 528px;
    background: var(--paper);
    overflow: hidden;
  }
  .letterhead .brand {
    position: absolute;
    left: 24px;
    top: 26px;
    display: flex;
    align-items: center;
    gap: 10px;
  }
  .brand-dot {
    width: 22px;
    height: 22px;
    border-radius: 50%;
    background: var(--brand-blue);
    flex: none;
  }
  .brand-name {
    font-weight: 300;
    font-size: 18px;
    letter-spacing: 3px;
    color: var(--ink-dark);
    text-transform: uppercase;
    white-space: nowrap;
  }
  .backdrop-ring {
    position: absolute;
    fill: none;
    pointer-events: none;
  }
  .letterhead .backdrop-ring {
    left: 0;
    top: 110px;
    width: 374px;
    height: 300px;
    stroke: var(--motif-light);
  }
  .letterhead-footer {
    position: absolute;
    left: 0;
    bottom: 0;
    width: 100%;
    height: 45px;
    background: var(--footer-band);
    display: flex;
    justify-content: space-between;
    align-items: center;
    padding: 0 22px 0 16px;
    box-sizing: border-box;
    font-size: 7px;
    letter-spacing: 0.4px;
    color: var(--ink-grey);
    text-transform: uppercase;
    line-height: 10px;
  }
  .contact-line {
    display: flex;
    align-items: center;
    gap: 5px;
    white-space: nowrap;
  }
  .contact-line svg { width: 6px; height: 6px; flex: none; }

  /* Folder, opened flat */
  .folder {
    position: absolute;
    left: 500px;
    top: 440px;
    width: 640px;
    height: 440px;
    display: flex;
    background: var(--folder-navy);
    overflow: hidden;
  }
  .folder .backdrop-ring {
    left: 0;
    top: 0;
    width: 640px;
    height: 440px;
    stroke: var(--motif-dark);
  }
  .folder-panel {
    position: relative;
    width: 320px;
    height: 100%;
  }
  .folder-panel.back {
    border-right: 1px solid var(--folder-fold);
  }
  .folder-contact {
    position: absolute;
    left: 34px;
    bottom: 48px;
    color: var(--folder-text);
    font-size: 7px;
    letter-spacing: 0.5px;
    text-transform: uppercase;
    line-height: 10px;
  }
  .folder-contact .brand {
    display: flex;
    align-items: center;
    gap: 7px;
    margin-bottom: 12px;
  }
  .folder-contact .brand-dot { width: 14px; height: 14px; }
  .folder-contact .brand-name {
    font-size: 12px;
    letter-spacing: 2px;
    color: var(--folder-text);
  }
  .folder-contact .address { margin-bottom: 6px; }
</style>
</head>
<body>
<main class="canvas">

  <section class="letterhead" aria-label="Letterhead">
    <svg class="backdrop-ring" viewBox="0 0 374 300" aria-hidden="true">
      <circle cx="285" cy="150" r="140" stroke-width="1"/>
    </svg>
    <div class="brand">
      <span class="brand-dot"></span>
      <span class="brand-name">Northgate Vision</span>
    </div>
    <footer class="letterhead-footer">
      <div class="contact">
        <div class="contact-line">
          <svg viewBox="0 0 10 10"><path d="M2 1 L4 1 L4.5 3.5 L3.2 4.3 Q4.3 6.3 5.8 6.8 L6.6 5.5 L9 6 L9 8 Q5 9.5 1.5 4.5 Q1 2.5 2 1 Z" fill="#6d6e70"/></svg>
          555-014-2290
        </div>
        <div class="contact-line">
          <svg viewBox="0 0 10 10"><circle cx="5" cy="5" r="4.5" fill="#6d6e70"/></svg>
          northgatevision.example
        </div>
      </div>
      <div class="address">
        1420 Linden Park Ave. Suite B<br>
        Ashford, OH 44010
      </div>
    </footer>
  </section>

  <section class="folder" aria-label="Presentation folder, outside spread">
    <svg class="backdrop-ring" viewBox="0 0 640 440" aria-hidden="true">
      <circle cx="450" cy="200" r="170" stroke-width="1"/>
    </svg>
    <div class="folder-panel back">
      <div class="folder-contact">
        <div class="brand">
          <span class="brand-dot"></span>
          <span class="brand-name">Northgate Vision</span>
        </div>
        <div class="address">
          1420 Linden Park Ave. Suite B<br>
          Ashford, OH 44010
        </div>
        <div class="contact-line">
          <svg viewBox="0 0 10 10"><path d="M2 1 L4 1 L4.5 3.5 L3.2 4.3 Q4.3 6.3 5.8 6.8 L6.6 5.5 L9 6 L9 8 Q5 9.5 1.5 4.5 Q1 2.5 2 1 Z" fill="#9fb3c2"/></svg>
          555-014-2290
        </div>
        <div class="contact-line">
          <svg viewBox="0 0 10 10"><circle cx="5" cy="5" r="4.5" fill="#9fb3c2"/></svg>
          northgatevision.example
        </div>
      </div>
    </div>
    <div class="folder-panel front"></div>
  </section>

</main>
</body>
</html>
```